Business Card Design Project

We are VT Meridian, a recruitment company based in London. We require a new business card design in order to present our business. We work in a number of areas recruiting professional in areas such as engineering and rail. Most of our work is based in the Middle East so our cards must have a universal, professional feel.

Visit our website: http://www.vt-meridian.example.co.uk/ for more info

Industry/Entity Type

Business

Requirements
Must have
• Must be double sided

Must feature the companies logo on both sides of the card

Should incorporate the primary colours of the logo

Must be professional and contemporary, to fit in with the logo

Info: Name: Colin Prewett certRP MREC
Senior Recruitment Consultant
Address: 7 Quarry Row Fulwell London N41QZ
T: +44 (0)203 555 0147
M: +44 (0)7700 900 318
E: cprewett@vt-meridian.example.co.uk
W www.vt-meridian.example.co.uk
Nice to have
• A modern style card

```html
<!DOCTYPE html>
<html lang="en">
<head>
<meta charset="utf-8">
<title>VT Meridian — Business Card</title>
<link rel="stylesheet" href="https://fonts.googleapis.com/css2?family=Montserrat:wght@400;600;700;800&display=swap">
<style>
  :root {
    --bg: #e9e7e1;
    --card-light: #eef3f1;
    --card-grey: #dcdcdc;
    --carbon: #2c2e30;
    --green: #2ee88a;
    --green-deep: #1fcf74;
    --ink: #1f1f1f;
    --brand-grey: #7d8184;
    --plate: #f1f1f1;
  }
  * { margin: 0; padding: 0; box-sizing: border-box; }
  html, body { width: 1200px; height: 1000px; overflow: hidden; }
  body {
    background: var(--bg);
    font-family: "Montserrat", Arial, sans-serif;
    position: relative;
  }
  .card {
    position: absolute;
    left: 280px;
    width: 640px;
    height: 360px;
    border-radius: 28px;
    overflow: hidden;
    box-shadow: 0 6px 18px rgba(0,0,0,.18);
  }
  .card--front { top: 100px; }
  .card--back { top: 540px; background: var(--card-grey); }
  .card__art { position: absolute; inset: 0; width: 100%; height: 100%; }

  .brand { position: absolute; display: flex; align-items: center; gap: 14px; }
  .brand__dot { border-radius: 50%; background: var(--green); flex: none; }
  .brand__name { color: var(--brand-grey); font-weight: 600; letter-spacing: -1px; line-height: 1; white-space: nowrap; }
  .tagline {
    position: absolute;
    color: var(--brand-grey);
    font-weight: 400;
    letter-spacing: 3px;
    text-transform: uppercase;
    white-space: nowrap;
  }
  .tagline__accent { color: var(--green-deep); }

  .card--front .brand { left: 96px; top: 86px; }
  .card--front .brand__dot { width: 62px; height: 62px; }
  .card--front .brand__name { font-size: 62px; }
  .card--front .tagline { left: 172px; top: 156px; font-size: 11px; }

  .address {
    position: absolute;
    left: 190px; top: 296px;
    display: flex; align-items: center; gap: 10px;
    font-size: 13px; font-weight: 700; color: var(--ink);
    text-transform: uppercase;
  }
  .address svg { width: 16px; height: 18px; }

  .plate {
    position: absolute;
    left: 180px; top: 34px;
    width: 320px; height: 82px;
    border-radius: 41px;
    background: var(--plate);
    box-shadow: inset 0 0 0 2px #cfcfcf;
  }
  .card--back .brand { left: 200px; top: 50px; gap: 10px; }
  .card--back .brand__dot { width: 40px; height: 40px; }
  .card--back .brand__name { font-size: 38px; }
  .card--back .tagline { left: 252px; top: 92px; font-size: 7px; letter-spacing: 2px; }

  .person { position: absolute; left: 56px; top: 196px; text-transform: uppercase; white-space: nowrap; }
  .person__name { font-size: 28px; font-weight: 800; color: var(--card-light); -webkit-text-stroke: 1px #555; letter-spacing: 1px; line-height: 34px; }
  .person__creds { font-size: 13px; font-weight: 700; color: var(--ink); -webkit-text-stroke: 0; letter-spacing: 0; }
  .person__title { font-size: 13px; font-weight: 700; color: var(--ink); margin-top: 2px; }

  .contacts {
    position: absolute; right: 36px;
    list-style: none;
    font-size: 13px; font-weight: 600; color: var(--ink);
    text-transform: uppercase; white-space: nowrap;
  }
  .contacts--phone { top: 140px; }
  .contacts--online { top: 256px; }
  .contacts li { height: 24px; display: flex; justify-content: flex-end; align-items: center; gap: 10px; }
  .contacts svg { width: 16px; height: 16px; flex: none; }
</style>
</head>
<body>

<section class="card card--front" aria-label="Business card front">
  <svg class="card__art" viewBox="0 0 640 360" preserveAspectRatio="none" aria-hidden="true">
    <rect width="640" height="360" fill="var(--carbon)"/>
    <ellipse cx="300" cy="190" rx="400" ry="205" transform="rotate(-14 300 190)" fill="var(--green)"/>
    <ellipse cx="305" cy="188" rx="392" ry="198" transform="rotate(-14 305 188)" fill="var(--card-light)"/>
  </svg>
  <div class="brand">
    <span class="brand__dot"></span>
    <span class="brand__name">VT Meridian</span>
  </div>
  <p class="tagline">Professional &amp; Technical <span class="tagline__accent">Recruitment</span></p>
  <p class="address">
    <svg viewBox="0 0 16 18"><path d="M8 1a6 6 0 0 0-6 6c0 4.5 6 10 6 10s6-5.5 6-10a6 6 0 0 0-6-6z" fill="none" stroke="var(--green-deep)" stroke-width="1.8"/><circle cx="8" cy="7" r="2" fill="var(--green-deep)"/></svg>
    7 Quarry Row Fulwell London N41QZ
  </p>
</section>

<section class="card card--back" aria-label="Business card back">
  <div class="plate"></div>
  <div class="brand">
    <span class="brand__dot"></span>
    <span class="brand__name">VT Meridian</span>
  </div>
  <p class="tagline">Professional &amp; Technical <span class="tagline__accent">Recruitment</span></p>

  <ul class="contacts contacts--phone">
    <li>+44 (0)203 555 0147
      <svg viewBox="0 0 16 16"><path d="M4 1l3 3-2 2a9 9 0 0 0 5 5l2-2 3 3-2 3C7 15 1 9 1 3z" fill="none" stroke="var(--green-deep)" stroke-width="1.6"/></svg>
    </li>
    <li>+44 (0)7700 900 318
      <svg viewBox="0 0 16 16"><rect x="4" y="1" width="8" height="14" rx="2" fill="none" stroke="var(--green-deep)" stroke-width="1.6"/><circle cx="8" cy="12.5" r="1" fill="var(--green-deep)"/></svg>
    </li>
  </ul>

  <div class="person">
    <p class="person__name">Colin Prewett <span class="person__creds">(Cert) RP MREC</span></p>
    <p class="person__title">Senior Recruitment Consultant</p>
  </div>

  <ul class="contacts contacts--online">
    <li>www.vt-meridian.example.co.uk
      <svg viewBox="0 0 16 16"><circle cx="8" cy="8" r="6.5" fill="none" stroke="var(--green-deep)" stroke-width="1.6"/><path d="M1.5 8h13M8 1.5c3 3.5 3 9.5 0 13M8 1.5c-3 3.5-3 9.5 0 13" fill="none" stroke="var(--green-deep)" stroke-width="1.2"/></svg>
    </li>
    <li>cprewett@vt-meridian.example.co.uk
      <svg viewBox="0 0 16 16"><circle cx="8" cy="8" r="2.8" fill="none" stroke="var(--green-deep)" stroke-width="1.6"/><path d="M10.8 5.5v4a1.8 1.8 0 0 0 3.6 0V8A6.4 6.4 0 1 0 11 13.5" fill="none" stroke="var(--green-deep)" stroke-width="1.6"/></svg>
    </li>
  </ul>
</section>

</body>
</html>
```